Networking card

I just need a simple design with the following information:
Ravin Doshu
318.647.2094
rdoshu583016@mailvanta.com

I would like to have a white background with blue text like in this sample: https://cardmintly.com/business-card-207346/

```html
<!DOCTYPE html>
<html lang="en">
<head>
<meta charset="utf-8">
<title>Ravin Doshu – Networking Card</title>
<link rel="stylesheet" href="https://fonts.googleapis.com/css2?family=Krona+One&family=Arimo:wght@400&display=swap">
<style>
  :root {
    --backdrop: #012136;
    --card: #ffffff;
    --brand-navy: #0b3a5c;
    --text-dark: #333333;
    --network-grey: #d6d6d6;
  }
  * { margin: 0; padding: 0; box-sizing: border-box; }
  html, body {
    width: 1200px;
    height: 1000px;
    overflow: hidden;
    background: var(--backdrop);
  }
  .business-card {
    position: absolute;
    left: 75px;
    top: 200px;
    width: 1050px;
    height: 600px;
    background: var(--card);
    border-radius: 28px;
    overflow: hidden;
  }
  .network-decoration {
    position: absolute;
    left: 612px;
    top: 0;
    width: 438px;
    height: 320px;
    background: radial-gradient(ellipse at 80% 20%, #e4e4e4 0%, #efefef 45%, rgba(255,255,255,0) 75%);
  }
  .holder-name {
    position: absolute;
    left: 115px;
    top: 238px;
    font-family: "Krona One", sans-serif;
    font-size: 38px;
    letter-spacing: 1px;
    color: var(--brand-navy);
    line-height: 1;
  }
  .contact-list {
    position: absolute;
    left: 115px;
    top: 331px;
    list-style: none;
  }
  .contact-item {
    display: flex;
    align-items: center;
    height: 43px;
    font-family: "Arimo", sans-serif;
    font-size: 26px;
    color: var(--text-dark);
  }
  .contact-icon {
    width: 36px;
    height: 32px;
    margin-right: 11px;
    flex: none;
  }
  .globe-emblem {
    position: absolute;
    left: 680px;
    top: 212px;
    width: 215px;
    height: 228px;
    border-radius: 50%;
    background: radial-gradient(circle at 45% 45%, #2c5a7c 0%, var(--brand-navy) 70%);
  }
</style>
</head>
<body>
  <main class="business-card">
    <div class="network-decoration" role="img" aria-label="Faint grey network of connected nodes and lines"></div>

    <h1 class="holder-name">RAVIN DOSHU</h1>

    <ul class="contact-list">
      <li class="contact-item">
        <svg class="contact-icon" viewBox="0 0 36 32" aria-hidden="true">
          <rect width="36" height="32" rx="4" fill="var(--brand-navy)"/>
          <rect x="12" y="6" width="12" height="20" rx="2" fill="none" stroke="#fff" stroke-width="2"/>
          <circle cx="18" cy="22.5" r="1.3" fill="#fff"/>
        </svg>
        318.647.2094
      </li>
      <li class="contact-item">
        <svg class="contact-icon" viewBox="0 0 36 32" aria-hidden="true">
          <rect width="36" height="32" rx="4" fill="var(--brand-navy)"/>
          <path d="M9 16 L27 8 L22 25 L17 19 Z" fill="#fff"/>
          <path d="M17 19 L27 8" stroke="var(--brand-navy)" stroke-width="1.5"/>
        </svg>
        rdoshu583016@mailvanta.com
      </li>
    </ul>

    <div class="globe-emblem" role="img" aria-label="Navy globe icon with connected network nodes"></div>
  </main>
</body>
</html>
```